Design a large parking banner – mandatory ticket validation in the shop

Banner Size:
548 cm (width) x 154 cm (height)
Note: The banner will be placed in a metal frame at our parking lot entrance, fully visible to every incoming truck driver. The message must be easy to read from a distance.
Goal of the Banner:
To inform all truck drivers that they must validate their entry ticket inside the shop, even if they are parking for a short time.
The message must be displayed in multiple languages for international drivers.
Mandatory Content:
Main message – in multiple languages (clearly separated or stacked):
Dutch (NL): Vergeet je ticket niet te valideren in de shop – verplicht, ook bij kort parkeren!
French (FR): N'oubliez pas de valider votre ticket à la boutique – obligatoire, même pour un court arrêt !
English (EN): Don't forget to validate your entry ticket in the shop – mandatory, even for short stops!
German (DE): Vergessen Sie nicht, Ihr Einfahrticket im Shop zu entwerten – Pflicht, auch bei kurzem Parken!
Polish (PL): Nie zapomnij zatwierdzić biletu w sklepie – obowiązkowe, nawet przy krótkim postoju!
Romanian (RO): Nu uitați să validați biletul în magazin – obligatoriu, chiar și pentru opriri scurte!
You can include more languages if space allows, but these are essential.
Opening Hours Block (in one section below):
Shop Opening Hours
Mon – Fri: 05:30 – 22:00
Sat & Sun: 08:00 – 22:00
Style & Branding:
The design must match the visual identity of Haulport 41Ter
Please refer to the attached photos of existing parking signage for guidance on colors, typography, and layout style
Our logo (attached) must be clearly visible and professionally integrated
Feel free to use icons or pictograms to visually support the message (e.g., ticket, truck, arrow)
Readability is key – large, bold text and high contrast colors that are visible from a distance
Target Audience:
International truck drivers – people who need fast, clear communication. Not everyone speaks the local language, so visual clarity and multilingual messaging are critical.
File Requirements:
Print-ready file (PDF or EPS) – 300 dpi at 1:10 scale
Include 5 cm bleed on all sides
Provide open source files if possible (AI or PSD)

```html
<!DOCTYPE html>
<html lang="en">
<head>
<meta charset="utf-8">
<title>Haulport 41Ter – Ticket Validation Banner</title>
<link href="https://fonts.googleapis.com/css2?family=Montserrat:ital,wght@1,700&family=Exo+2:ital,wght@1,800&display=swap" rel="stylesheet">
<style>
  :root {
    --backdrop: #9a9a9a;
    --paper: #ffffff;
    --navy: #1b1f5e;
    --red: #d42030;
    --band-light: #27357f;
    --band-dark: #0c144b;
    --rule: #7a7a84;
    --white: #ffffff;
  }
  html, body {
    margin: 0;
    width: 1200px;
    height: 408px;
    overflow: hidden;
    background: var(--backdrop);
  }
  .banner {
    position: absolute;
    left: 68px;
    top: 56px;
    width: 1066px;
    height: 296px;
    background: var(--paper);
    overflow: hidden;
  }
  .messages {
    position: absolute;
    left: 0; top: 0;
    width: 100%;
    height: 186px;
    margin: 0; padding: 0;
    list-style: none;
  }
  .message {
    position: absolute;
    left: 0; width: 100%;
    height: 29px;
    display: flex;
    align-items: center;
    justify-content: center;
    font-family: "Montserrat", sans-serif;
    font-weight: 700;
    font-style: italic;
    font-size: 16.6px;
    letter-spacing: -0.1px;
    color: var(--navy);
    white-space: pre;
    border-bottom: 1px solid var(--rule);
  }
  .message:last-child { border-bottom: none; }
  .message .rule-note { color: var(--red); }
  .message:nth-child(1) { top: 8.6px; }
  .message:nth-child(2) { top: 38.2px; }
  .message:nth-child(3) { top: 67px; }
  .message:nth-child(4) { top: 95.8px; }
  .message:nth-child(5) { top: 125.4px; }
  .message:nth-child(6) { top: 153.4px; }

  .hours-band {
    position: absolute;
    left: 0; top: 186px;
    width: 100%;
    height: 110px;
    background: linear-gradient(90deg, var(--band-light), var(--band-dark));
  }
  .hours-title {
    position: absolute;
    left: 48px; top: 14px;
    margin: 0;
    font-family: "Exo 2", sans-serif;
    font-weight: 800;
    font-style: italic;
    font-size: 36px;
    line-height: 36px;
    color: var(--white);
    text-transform: uppercase;
  }
  .hours-row {
    position: absolute;
    left: 330px;
    height: 40px;
    width: 436px;
    font-family: "Exo 2", sans-serif;
    font-weight: 800;
    font-style: italic;
    font-size: 31px;
    text-transform: uppercase;
  }
  .hours-row.weekdays { top: 8px; }
  .hours-row.weekend { top: 52px; }
  .hours-days, .hours-time {
    position: absolute;
    top: 0; height: 100%;
    display: flex;
    align-items: center;
    justify-content: center;
  }
  .hours-days {
    left: 0; width: 200px;
    background: var(--white);
    color: var(--navy);
    clip-path: polygon(10px 0, 100% 0, calc(100% - 10px) 100%, 0 100%);
  }
  .hours-time {
    left: 188px; width: 248px;
    background: var(--red);
    color: var(--white);
    clip-path: polygon(10px 0, 100% 0, calc(100% - 10px) 100%, 0 100%);
  }
  .brand-name {
    position: absolute;
    left: 796px; top: 36px;
    width: 210px;
    text-align: center;
    font-family: "Exo 2", sans-serif;
    font-weight: 800;
    font-style: italic;
    font-size: 32px;
    line-height: 38px;
    color: var(--white);
    text-transform: uppercase;
  }
</style>
</head>
<body>
  <main class="banner">
    <ul class="messages">
      <li class="message" lang="nl">Vergeet je ticket niet te valideren in de shop – <span class="rule-note">verplicht, ook bij kort parkeren!</span></li>
      <li class="message" lang="fr">N'oubliez pas de valider votre ticket à la boutique – <span class="rule-note">obligatoire, même pour un court arrêt !</span></li>
      <li class="message" lang="en">Don't forget to validate your entry ticket in the shop – <span class="rule-note">mandatory, even for short stops!</span></li>
      <li class="message" lang="de">Vergessen Sie nicht, Ihr Einfahrticket im Shop zu entwerten – <span class="rule-note">Pflicht, auch bei kurzem Parken!</span></li>
      <li class="message" lang="pl">Nie zapomnij zatwierdzić biletu w sklepie – <span class="rule-note">obowiązkowe, nawet przy krótkim postoju!</span></li>
      <li class="message" lang="ro">Nu uitați să validați biletul în magazin – <span class="rule-note">obligatoriu, chiar și pentru opriri scurte!</span></li>
    </ul>
    <section class="hours-band">
      <h2 class="hours-title">Shop Opening<br>Hours</h2>
      <div class="hours-row weekdays">
        <span class="hours-days">Mon — Fri:</span>
        <span class="hours-time">05:30 — 22:00</span>
      </div>
      <div class="hours-row weekend">
        <span class="hours-days">Sat &amp; Sun:</span>
        <span class="hours-time">08:00 — 22:00</span>
      </div>
      <div class="brand-name">Haulport 41Ter</div>
    </section>
  </main>
</body>
</html>
```